Bright Ridge Metals is a new gold exploration company. Their mandate is discovering new gold deposits.
Bright Ridge Metals will need to make public presentations and send out news releases on company letterheads.

We have recently designed a logo.

What we need:
We need a Powerpoint Template and Word template for corporate communications.

We need you to:

0) Provide a Corporate Colour Palette / Colour Swatch that we can load into powerpoint as our colour palette.

1) Using that colour palette, design a POWERPOINT presentation TEMPLATE that works with our logo – and works with but doesn't necessarily require Trajan Pro font. We’ll need a slide background, image and text layout, text-image balance, recommended font size, colours, composition

2) We’ll want to see your Powerpoint templates – we need Front page, Content Page, Divider Page, Back page with a good background, header, footer, and layout
--> Deliverable is a Powerpoint Template design file including colour palette that will automatically assign colours to charts / graphs, background, text etc

3) We’ll want to see your WORD REPORT templates – we need a Front page, Content Page, Divider Page, Back page with a good background, header, footer, title, section heading and sub-section font styles and layout for lengthy company reports. Note our logo is in Trajan Pro.

4) AND we need a LETTERHEAD (Word template) with front page header, footer, memo layout and subsequent pages with header and footer.

and 5) An EMAIL SIGNATURE
Please supply results as POWERPOINT and WORD

We want to see inverted colour ideas as well (our logo shows blacktext, we'd like to see ideas with White text (or another colour that works)

For colour ideas and a contribution to our Divider page we have loaded up photographs in a .pptx file below. These are the sorts of hues many of our future photos will generate.. please keep it in mind.

Our upload also shows some constraints - logo bottom left - only use 2.72cm in your banner.. etc.. it's all there

Do a great job and there may be more to come - we also need to build a new website

It's a challenge, but we've seen what sketch hive can do and we know you can make something great with what we have.

Do what you can.. we may award even if not all items are complete.
Start with Colour Palette, Email signature and Letterhead.
Then Powerpoint.
Word can be last.

Looking forward to it...

Target Market(s)

Investors that expect to see corporate presentations with a style and professional look that you see from companies like Tarvenne Holdings, KPL, gold exploration, Halverine, Corvanta, Ostralyn, Pelorik Gold, Tamsey, Gold Venn, etc...

Industry/Entity Type

Mining

Font styles to use
Serif
Sans Serif

Requirements
Must have
• A colour palette that can be applied in PowerPoint Design tab
• A PowerPoint Template .POTX file
• - Title page
• - Content page
• - Divider page
• - Backpage
• no more than 2.75cm banner, no more than 1.5cm footer
• follow instructions as shown in .pdf upload (content slide title position, logo position - others are flexible
• Must use logo uploaded
• Email signature (.eps, .ai, .png files)
• Word letterhead (.docx and .DOTX)
• *Update - 1st Feb - Business cards are to be Embossed with Sunken lettering
Nice to have
• Layout recommendations - example showing text / image balance
Should not have
• australia flag, southern cross, kangaroos...

```html
<!DOCTYPE html>
<html lang="en">
<head>
<meta charset="utf-8">
<title>Bright Ridge Metals Corp – Business Card</title>
<link rel="stylesheet" href="https://fonts.googleapis.com/css2?family=Cinzel:wght@400;600&family=Open+Sans:wght@400;700&display=swap">
<style>
  :root {
    --page-bg: #e2e2e2;
    --card-bg: #f7f7f6;
    --gold: #a8872f;
    --ink: #4b4a45;
    --text: #4d4d4d;
    --label: #111111;
  }
  * { margin: 0; padding: 0; box-sizing: border-box; }
  html, body { width: 965px; height: 1200px; overflow: hidden; }
  body {
    position: relative;
    background: var(--page-bg);
    font-family: "Open Sans", Arial, sans-serif;
    color: var(--text);
  }
  .card {
    position: absolute;
    left: 73px;
    width: 815px;
    height: 489px;
    background: var(--card-bg);
  }
  .card--front { top: 45px; }
  .card--back { top: 615px; }
  .side-label {
    position: absolute;
    left: 0;
    width: 965px;
    text-align: center;
    font-size: 24px;
    letter-spacing: 2.5px;
    color: var(--label);
  }
  .side-label--front { top: 549px; }
  .side-label--back { top: 1124px; }

  .brand {
    position: absolute;
    left: 0;
    width: 100%;
    display: flex;
    align-items: center;
    justify-content: center;
    transform: translateY(-50%);
  }
  .brand__dot { border-radius: 50%; background: var(--gold); flex: none; }
  .brand__name {
    font-family: "Cinzel", "Times New Roman", serif;
    font-weight: 600;
    color: var(--ink);
    line-height: 1.1;
  }
  .card--front .brand { top: 107px; gap: 16px; }
  .card--front .brand__dot { width: 54px; height: 54px; }
  .card--front .brand__name { font-size: 28px; }
  .card--back .brand { top: 245px; gap: 26px; }
  .card--back .brand__dot { width: 92px; height: 92px; }
  .card--back .brand__name { font-size: 46px; }

  .person {
    position: absolute;
    top: 205px;
    left: 0;
    width: 100%;
    text-align: center;
  }
  .person__name {
    font-family: "Cinzel", "Times New Roman", serif;
    font-weight: 600;
    font-size: 31px;
    line-height: 34px;
    color: var(--gold);
  }
  .person__role {
    margin-top: 5px;
    font-size: 15px;
    letter-spacing: 0.3px;
    color: var(--text);
  }

  .contact {
    position: absolute;
    display: flex;
    align-items: center;
    gap: 11px;
    font-size: 16px;
    white-space: nowrap;
    transform: translateY(-50%);
  }
  .contact svg { width: 26px; height: 26px; flex: none; }
  .contact--bold { font-weight: 700; }
  .contact--phone { left: 53px; top: 362px; }
  .contact--address { left: 53px; top: 410px; }
  .contact--email { left: 452px; top: 362px; }
  .contact--web { left: 452px; top: 410px; }
</style>
</head>
<body>

<section class="card card--front">
  <div class="brand">
    <span class="brand__dot"></span>
    <div class="brand__name">Bright Ridge<br>Metals Corp</div>
  </div>

  <div class="person">
    <div class="person__name">CORIN MALLET</div>
    <div class="person__role">DIRECTOR</div>
  </div>

  <div class="contact contact--phone contact--bold">
    <svg viewBox="0 0 26 26" aria-hidden="true">
      <circle cx="13" cy="13" r="13" fill="var(--gold)"/>
      <path d="M9.2 6.5c.6-.3 1.2-.1 1.5.4l1.3 2.3c.3.5.2 1.1-.3 1.5l-.9.7c.6 1.5 1.8 2.8 3.3 3.5l.7-.9c.4-.5 1-.6 1.5-.3l2.3 1.3c.5.3.7 1 .4 1.5l-.8 1.3c-.4.6-1.1.9-1.8.8-4.3-.8-7.6-4.1-8.4-8.4-.1-.7.2-1.4.8-1.8z" fill="#fff"/>
    </svg>
    <span>+61 7 3940 2715</span>
  </div>

  <div class="contact contact--address">
    <svg viewBox="0 0 26 26" aria-hidden="true">
      <circle cx="13" cy="13" r="13" fill="var(--gold)"/>
      <path d="M13 5.5a5 5 0 0 0-5 5c0 3.8 5 9.5 5 9.5s5-5.7 5-9.5a5 5 0 0 0-5-5z" fill="#fff"/>
      <circle cx="13" cy="10.5" r="2" fill="var(--gold)"/>
    </svg>
    <span>8/3 Keel Street, Ashgrove, Queensland 4060</span>
  </div>

  <div class="contact contact--email contact--bold">
    <svg viewBox="0 0 26 26" aria-hidden="true">
      <rect x="1" y="6" width="24" height="15" fill="var(--gold)"/>
      <path d="M1 6l12 9 12-9M1 21l9-7.5M25 21l-9-7.5" fill="none" stroke="#fff" stroke-width="1.4"/>
    </svg>
    <span>cmallet@brightridgemetals.com</span>
  </div>

  <div class="contact contact--web">
    <svg viewBox="0 0 26 26" aria-hidden="true">
      <g fill="none" stroke="var(--gold)" stroke-width="1.4">
        <circle cx="13" cy="13" r="11.5"/>
        <ellipse cx="13" cy="13" rx="5" ry="11.5"/>
        <path d="M1.5 13h23M13 1.5v23M3.5 7h19M3.5 19h19"/>
      </g>
    </svg>
    <span>www.brightridgemetals.com</span>
  </div>
</section>
<div class="side-label side-label--front">FRONT SIDE</div>

<section class="card card--back">
  <div class="brand">
    <span class="brand__dot"></span>
    <div class="brand__name">Bright Ridge<br>Metals Corp</div>
  </div>
</section>
<div class="side-label side-label--back">BACK SIDE</div>

</body>
</html>
```